Banner poster with different motifs

I'm looking for 5 banners and posters in A1 format in the same design, or the similarity must be recognizable...
Kept quite simple with different titles.

1 ballet
2 Contemporary Dance
3 high heels
4 Salsa & Bachata & Zouk
5 Hip Hop

Modern bright colors
it is for the entrance so that the students see here is a dance school

The text may also be included in the image
The photos are for guidance only; some are our own, some are purchased. However, we are permitted to use them, including our logo, of course.

```html
<!DOCTYPE html>
<html lang="de">
<head>
<meta charset="utf-8">
<title>Salsa, Bachata &amp; Zouk – Movimiento Dance Center</title>
<link rel="stylesheet" href="https://fonts.googleapis.com/css2?family=Antonio:wght@700&family=Kaushan+Script&family=Archivo+Black&family=Montserrat:wght@400;500&family=Playfair+Display:wght@700&display=swap">
<style>
  :root {
    --ink: #0b0605;
    --smoke: #4a2e24;
    --glow: #b88a00;
    --gold: #f7dc12;
    --amber: #f2b233;
    --flame: #f25a12;
    --white: #ffffff;
    --silver: #c9c9c9;
    --brown: #6e3316;
    --cream: #f5e4b2;
  }
  html, body {
    margin: 0;
    width: 850px;
    height: 1200px;
    overflow: hidden;
    background: var(--ink);
  }
  .poster {
    display: block;
    width: 850px;
    height: 1200px;
  }
  .brand-name {
    font-family: "Montserrat", sans-serif;
    font-weight: 400;
    fill: var(--white);
  }
  .title-salsa { font-family: "Antonio", sans-serif; font-weight: 700; }
  .title-bachata { font-family: "Kaushan Script", cursive; }
  .title-zouk { font-family: "Archivo Black", sans-serif; fill: var(--white); }
  .amp { font-family: "Playfair Display", serif; font-weight: 700; fill: var(--brown); }
  .web { font-family: "Montserrat", sans-serif; font-weight: 500; }
</style>
</head>
<body>
<svg class="poster" viewBox="0 0 850 1200" xmlns="http://www.w3.org/2000/svg">
  <defs>
    <radialGradient id="glow-top-left" cx="0" cy="0" r="0.45">
      <stop offset="0" stop-color="var(--glow)"/>
      <stop offset="1" stop-color="var(--glow)" stop-opacity="0"/>
    </radialGradient>
    <radialGradient id="glow-bottom-right" cx="1" cy="1" r="0.4">
      <stop offset="0" stop-color="var(--glow)"/>
      <stop offset="1" stop-color="var(--glow)" stop-opacity="0"/>
    </radialGradient>
    <radialGradient id="photo-tone" cx="0.55" cy="0.5" r="0.6">
      <stop offset="0" stop-color="#7a6a60"/>
      <stop offset="0.45" stop-color="var(--smoke)"/>
      <stop offset="1" stop-color="var(--ink)"/>
    </radialGradient>
    <linearGradient id="salsa-fill" x1="0" y1="0" x2="0" y2="1">
      <stop offset="0" stop-color="var(--amber)"/>
      <stop offset="0.55" stop-color="var(--gold)"/>
      <stop offset="1" stop-color="#f5e000"/>
    </linearGradient>
    <linearGradient id="bachata-fill" x1="0" y1="0" x2="0" y2="1">
      <stop offset="0.2" stop-color="var(--white)"/>
      <stop offset="1" stop-color="var(--silver)"/>
    </linearGradient>
  </defs>

  <rect class="background" width="850" height="1200" fill="var(--ink)"/>

  <rect class="hero-photo" role="img" aria-label="Photo of a couple dancing bachata in a close embrace against a dark smoky backdrop"
        x="0" y="0" width="850" height="676" fill="url(#photo-tone)"/>

  <rect class="corner-glow" width="850" height="1200" fill="url(#glow-top-left)"/>
  <rect class="corner-glow" width="850" height="1200" fill="url(#glow-bottom-right)"/>

  <g class="brand">
    <circle cx="697" cy="90" r="42" fill="none" stroke="var(--white)" stroke-width="1.5"/>
    <text class="brand-name" x="698" y="172" font-size="34" text-anchor="middle" textLength="232" lengthAdjust="spacingAndGlyphs">MOVIMIENTO</text>
    <text class="brand-name" x="698" y="194" font-size="11" text-anchor="middle" letter-spacing="3.2">DANCE CENTER FRANKFURT</text>
  </g>

  <text class="title-salsa" x="200" y="793" font-size="330" fill="url(#salsa-fill)" textLength="450" lengthAdjust="spacingAndGlyphs">Salsa</text>

  <text class="title-bachata" x="160" y="890" font-size="176" fill="url(#bachata-fill)" stroke="var(--ink)" stroke-width="3" paint-order="stroke" textLength="550" lengthAdjust="spacingAndGlyphs">bachata</text>

  <g class="zouk-label">
    <rect x="235" y="888" width="372" height="138" fill="var(--brown)"/>
    <circle cx="275" cy="956" r="30" fill="var(--cream)"/>
    <text class="amp" x="275" y="974" font-size="50" text-anchor="middle">&amp;</text>
    <text class="title-zouk" x="310" y="992" font-size="112" textLength="276" lengthAdjust="spacingAndGlyphs">ZOUK</text>
  </g>

  <text class="web" x="425" y="1110" font-size="25" text-anchor="middle" letter-spacing="9">
    <tspan fill="var(--white)">www.</tspan><tspan fill="var(--gold)">movimiento</tspan><tspan fill="var(--white)">.de</tspan>
  </text>
</svg>
</body>
</html>
```